Small Box Design - For launch into retail market

We need artwork for small boxes that we are going to be using for the retail market. I will upload the type of box we are going to be using. The example we are uploading is of a different company that sells the same products. We would like our Logo on the box as as our web address (www.brandellgroup-ltd.com). The rest is up to you. Please contact with any questions.

Target Market(s)

Distributors, Retailers of Fasteners

Industry/Entity Type

Manufacture

Colors
0355a3
3176b5
fbee3f
fbf289

Requirements
Must have
• Our logo, our web address www.brandellgroup-ltd.com
• Somewhere on the box Washers . Stampings . Assemblies . Bearings (most likely below our logo somewhere)
Nice to have
• Blue is our corporate colour, but it's not essential. You can suggest any colours and we will consider.

```html
<!DOCTYPE html>
<html lang="en">
<head>
<meta charset="utf-8">
<title>Brandell Limited – Retail Carton Dieline</title>
<link rel="stylesheet" href="https://fonts.googleapis.com/css2?family=Questrial&family=Montserrat:wght@400;600;700&display=swap">
<style>
  :root {
    --page-bg: #f1f1f1;
    --carton-gold: #e9a62a;
    --carton-amber: #c8761a;
    --carton-rust: #a8521f;
    --carton-maroon: #7c2116;
    --glow: #fff4c8;
    --fold-line: rgba(255, 255, 255, 0.7);
    --brand-yellow: #fff200;
    --ink-white: #ffffff;
    --panel-ink: #fdf1d6;
  }
  html, body {
    margin: 0;
    padding: 0;
    width: 1016px;
    height: 1200px;
    overflow: hidden;
    background: var(--page-bg);
  }
  .dieline {
    display: block;
    width: 1016px;
    height: 1200px;
  }
  .carton-face { fill: url(#cartonTone); }
  .carton-glow { fill: url(#centreGlow); pointer-events: none; }
  .carton-glow--low { fill: url(#lowerGlow); }
  .fold { stroke: var(--fold-line); stroke-width: 1; fill: none; }
  .brand-name {
    font-family: "Questrial", sans-serif;
    font-size: 46px;
    fill: var(--ink-white);
  }
  .brand-sub {
    font-family: "Questrial", sans-serif;
    font-size: 12px;
    letter-spacing: 1px;
    fill: var(--ink-white);
  }
  .brand-dot { fill: var(--brand-yellow); }
  .web-address {
    font-family: "Montserrat", sans-serif;
    font-weight: 700;
    font-size: 12px;
    fill: var(--brand-yellow);
  }
  .product-line {
    font-family: "Montserrat", sans-serif;
    font-weight: 600;
    font-size: 9px;
    letter-spacing: 0.5px;
    fill: var(--ink-white);
  }
  .panel-headline {
    font-family: "Montserrat", sans-serif;
    font-weight: 600;
    font-size: 8px;
    fill: var(--panel-ink);
  }
  .panel-copy {
    font-family: "Montserrat", sans-serif;
    font-weight: 400;
    font-size: 7.4px;
    fill: var(--panel-ink);
  }
  .carton-number {
    font-family: "Montserrat", sans-serif;
    font-weight: 700;
    font-size: 22px;
    fill: var(--ink-white);
  }
  .carton-label {
    font-family: "Montserrat", sans-serif;
    font-weight: 700;
    font-size: 5px;
    fill: var(--ink-white);
  }
  .recycle-mark { stroke: var(--ink-white); stroke-width: 7; fill: none; }
  .recycle-head { fill: var(--ink-white); }
</style>
</head>
<body>
<svg class="dieline" viewBox="0 0 1158 1368" preserveAspectRatio="xMidYMid meet" xmlns="http://www.w3.org/2000/svg" role="img" aria-label="Flat dieline of the Brandell Limited retail carton">
  <defs>
    <linearGradient id="cartonTone" gradientUnits="userSpaceOnUse" x1="145" y1="0" x2="1020" y2="0">
      <stop offset="0" stop-color="var(--carton-amber)"/>
      <stop offset="0.18" stop-color="var(--carton-gold)"/>
      <stop offset="0.36" stop-color="#f2b53a"/>
      <stop offset="0.52" stop-color="var(--carton-rust)"/>
      <stop offset="0.7" stop-color="#8a2c18"/>
      <stop offset="1" stop-color="var(--carton-maroon)"/>
    </linearGradient>
    <radialGradient id="centreGlow" gradientUnits="userSpaceOnUse" cx="470" cy="380" r="230">
      <stop offset="0" stop-color="var(--glow)" stop-opacity="0.85"/>
      <stop offset="0.4" stop-color="#f6c24a" stop-opacity="0.45"/>
      <stop offset="1" stop-color="#f6c24a" stop-opacity="0"/>
    </radialGradient>
    <radialGradient id="lowerGlow" gradientUnits="userSpaceOnUse" cx="420" cy="800" r="180">
      <stop offset="0" stop-color="var(--glow)" stop-opacity="0.9"/>
      <stop offset="0.45" stop-color="#f6c24a" stop-opacity="0.4"/>
      <stop offset="1" stop-color="#f6c24a" stop-opacity="0"/>
    </radialGradient>
    <filter id="liftShadow" x="-5%" y="-5%" width="110%" height="110%">
      <feDropShadow dx="0" dy="2" stdDeviation="3" flood-color="#000" flood-opacity="0.3"/>
    </filter>
    <path id="panelLid" d="M405,88 H760 C835,92 902,140 902,210 C902,262 880,287 838,287 H326 C285,287 262,270 262,240 C262,150 330,95 405,88 Z"/>
    <rect id="panelSpine" x="403" y="284" width="359" height="700"/>
    <path id="panelFlapLeft" d="M155,365 H245 L258,352 H305 L318,365 H403 V540 H155 Z"/>
    <path id="panelFlapRight" d="M762,365 H845 L858,352 H905 L918,365 H1008 V540 H762 Z"/>
    <rect id="panelWall" x="145" y="540" width="875" height="290"/>
    <rect id="panelBase" x="145" y="980" width="875" height="205"/>
    <clipPath id="cartonOutline">
      <use href="#panelLid"/>
      <use href="#panelSpine"/>
      <use href="#panelFlapLeft"/>
      <use href="#panelFlapRight"/>
      <use href="#panelWall"/>
      <use href="#panelBase"/>
    </clipPath>
  </defs>

  <g class="carton" filter="url(#liftShadow)">
    <use class="carton-face lid" href="#panelLid"/>
    <use class="carton-face spine" href="#panelSpine"/>
    <use class="carton-face flap flap--left" href="#panelFlapLeft"/>
    <use class="carton-face flap flap--right" href="#panelFlapRight"/>
    <use class="carton-face wall-band" href="#panelWall"/>
    <use class="carton-face base-band" href="#panelBase"/>
  </g>

  <g class="carton-light" aria-hidden="true" clip-path="url(#cartonOutline)">
    <rect class="carton-glow" x="262" y="88" width="640" height="740"/>
    <rect class="carton-glow carton-glow--low" x="145" y="560" width="617" height="420"/>
  </g>

  <g class="folds">
    <path class="fold" d="M411,95 V1175 M752,95 V1175"/>
    <path class="fold" d="M411,282 H752 M411,95 H752"/>
    <path class="fold" d="M163,540 V372 H403 M1000,540 V372 H762"/>
    <path class="fold" d="M152,540 H1012 M152,728 H1012 M152,540 V822 M1012,540 V822"/>
    <path class="fold" d="M152,990 H1012 V1175 H152 Z"/>
    <path class="fold" d="M275,280 C268,250 270,170 330,120 C360,100 390,96 405,96"/>
    <path class="fold" d="M760,96 C830,100 892,145 892,210 C892,255 872,277 838,277 H762"/>
  </g>

  <g class="brand-panel" transform="translate(280 0)">
    <circle class="brand-dot" cx="-92" cy="630" r="9"/>
    <text class="brand-name" x="8" y="643" text-anchor="middle">Brandell</text>
    <text class="brand-sub" x="30" y="658" text-anchor="middle">LIMITED</text>
    <text class="web-address" x="0" y="693" text-anchor="middle" textLength="224" lengthAdjust="spacing">www.brandellgroup-ltd.com</text>
    <text class="product-line" x="0" y="712" text-anchor="middle" textLength="224" lengthAdjust="spacing">Washers . Stampings . Assemblies . Bearings</text>
  </g>
  <g class="brand-panel" transform="translate(582 0)">
    <circle class="brand-dot" cx="-92" cy="630" r="9"/>
    <text class="brand-name" x="8" y="643" text-anchor="middle">Brandell</text>
    <text class="brand-sub" x="30" y="658" text-anchor="middle">LIMITED</text>
    <text class="web-address" x="0" y="693" text-anchor="middle" textLength="224" lengthAdjust="spacing">www.brandellgroup-ltd.com</text>
    <text class="product-line" x="0" y="712" text-anchor="middle" textLength="224" lengthAdjust="spacing">Washers . Stampings . Assemblies . Bearings</text>
  </g>
  <g class="brand-panel" transform="translate(882 0)">
    <circle class="brand-dot" cx="-92" cy="630" r="9"/>
    <text class="brand-name" x="8" y="643" text-anchor="middle">Brandell</text>
    <text class="brand-sub" x="30" y="658" text-anchor="middle">LIMITED</text>
    <text class="web-address" x="0" y="693" text-anchor="middle" textLength="224" lengthAdjust="spacing">www.brandellgroup-ltd.com</text>
    <text class="product-line" x="0" y="712" text-anchor="middle" textLength="224" lengthAdjust="spacing">Washers . Stampings . Assemblies . Bearings</text>
  </g>

  <g class="info-panel" transform="rotate(180 582 188)">
    <circle class="brand-dot" cx="498" cy="140" r="8"/>
    <text class="brand-name" x="588" y="152" text-anchor="middle" style="font-size:40px">Brandell</text>
    <text class="brand-sub" x="606" y="167" text-anchor="middle" style="font-size:10px">LIMITED</text>
    <text class="web-address" x="582" y="201" text-anchor="middle" textLength="270" lengthAdjust="spacing">www.brandellgroup-ltd.com</text>
    <text class="panel-headline" x="582" y="218" text-anchor="middle">BRANDELL IS NOT JUST ANOTHER WASHER MANUFACTURER</text>
    <text class="panel-copy" x="582" y="229" text-anchor="middle">Brandell is recognized as a pioneer in the design of innovative stamping</text>
    <text class="panel-copy" x="582" y="239" text-anchor="middle">equipment. We have made our name through exceptional quality,</text>
    <text class="panel-copy" x="582" y="249" text-anchor="middle">our astute knowledge, and an enthusiastic desire to drive technology.</text>
  </g>

  <g class="info-panel" transform="rotate(180 582 1068)">
    <circle class="brand-dot" cx="498" cy="1020" r="8"/>
    <text class="brand-name" x="588" y="1032" text-anchor="middle" style="font-size:40px">Brandell</text>
    <text class="brand-sub" x="606" y="1047" text-anchor="middle" style="font-size:10px">LIMITED</text>
    <text class="web-address" x="582" y="1081" text-anchor="middle" textLength="270" lengthAdjust="spacing">www.brandellgroup-ltd.com</text>
    <text class="panel-headline" x="582" y="1098" text-anchor="middle">BRANDELL IS NOT JUST ANOTHER WASHER MANUFACTURER</text>
    <text class="panel-copy" x="582" y="1109" text-anchor="middle">Brandell is recognized as a pioneer in the design of innovative stamping</text>
    <text class="panel-copy" x="582" y="1119" text-anchor="middle">equipment. We have made our name through exceptional quality,</text>
    <text class="panel-copy" x="582" y="1129" text-anchor="middle">our astute knowledge, and an enthusiastic desire to drive technology.</text>
  </g>

  <g class="carton-id" transform="rotate(180 532 865)">
    <text class="carton-number" x="532" y="869" text-anchor="middle">4</text>
    <text class="carton-label" x="532" y="877" text-anchor="middle">CARTON</text>
  </g>
  <g class="recycle" aria-label="Recycling symbol" role="img">
    <path class="recycle-mark" d="M570,845 A30,30 0 0 1 620,848"/>
    <path class="recycle-mark" d="M627,866 A30,30 0 0 1 605,893"/>
    <path class="recycle-mark" d="M585,893 A30,30 0 0 1 565,862"/>
    <path class="recycle-head" d="M614,838 L630,852 L610,858 Z"/>
    <path class="recycle-head" d="M612,884 L610,903 L596,890 Z"/>
    <path class="recycle-head" d="M556,868 L566,852 L575,868 Z"/>
  </g>
</svg>
</body>
</html>
```